Woman owned consulting company needs an elegant and modern business card design

I need a business card design for my new consulting company, Mara Quill Consulting. I am looking for something that is simple and elegant, but also creative and original. You can use either version of the logo that are attached. I have also included the information that needs to be featured on the business card.

Requirements
Must have
• The logo and the font type and a standard business card size. Use shades of gray/silver and or rose gold that are in the logo.
• I didn't realize that my actual logo wasn't attached. Please incorporate in the designs.
Should not have
• Colors that are different from my logo

```html
<!DOCTYPE html>
<html lang="en">
<head>
<meta charset="utf-8">
<title>Mara Quill Consulting – Business Cards</title>
<link rel="stylesheet" href="https://fonts.googleapis.com/css2?family=Cinzel:wght@400;700&family=Libre+Baskerville&display=swap">
<style>
  :root {
    --backdrop: #d3d3d3;
    --card: #f7f7f6;
    --silver: #9a9a9a;
    --silver-light: #b4b4b4;
    --ink: #2b2b2b;
    --ink-soft: #555555;
  }
  * { box-sizing: border-box; margin: 0; padding: 0; }
  html, body { width: 1200px; height: 852px; overflow: hidden; }
  body {
    background: var(--backdrop);
    position: relative;
    font-family: "Libre Baskerville", Georgia, serif;
  }
  .card {
    position: absolute;
    top: 283px;
    width: 500px;
    height: 286px;
    background: var(--card);
    border-radius: 14px;
    box-shadow: 0 2px 8px rgba(0,0,0,0.12);
  }
  .card--front { left: 60px; }
  .card--back { left: 640px; }

  /* front */
  .brand {
    position: absolute;
    left: 0; right: 0; top: 98px;
    display: flex;
    align-items: center;
    justify-content: center;
    gap: 14px;
  }
  .brand__dot {
    width: 14px; height: 14px;
    border-radius: 50%;
    background: var(--silver);
  }
  .brand__name {
    font-family: "Cinzel", "Times New Roman", serif;
    font-weight: 400;
    font-size: 24px;
    letter-spacing: 2px;
    line-height: 1.15;
    color: var(--silver);
  }
  .front__web {
    position: absolute;
    right: 0; left: 0; bottom: 58px;
    text-align: center;
    font-size: 12px;
    color: var(--ink-soft);
  }

  /* back */
  .back__mark {
    position: absolute;
    right: 34px; top: 30px;
    font-family: "Cinzel", "Times New Roman", serif;
    font-weight: 400;
    font-size: 40px;
    letter-spacing: 3px;
    color: var(--silver-light);
  }
  .holder {
    position: absolute;
    left: 36px; top: 120px;
  }
  .holder__name {
    font-family: "Cinzel", "Times New Roman", serif;
    font-weight: 700;
    font-size: 17px;
    letter-spacing: 1px;
    color: var(--ink);
  }
  .holder__role {
    font-size: 11px;
    color: var(--ink-soft);
    margin-top: 2px;
  }
  .contact {
    position: absolute;
    left: 36px; bottom: 30px;
    list-style: none;
  }
  .contact__item {
    display: flex;
    align-items: center;
    gap: 10px;
    font-size: 11.5px;
    color: var(--ink);
    line-height: 19px;
  }
  .contact__icon { width: 11px; height: 11px; fill: var(--ink); }
</style>
</head>
<body>
  <section class="card card--front" aria-label="Card front">
    <div class="brand">
      <span class="brand__dot"></span>
      <span class="brand__name">Mara Quill<br>Consulting, LLC</span>
    </div>
    <p class="front__web">www.maraquillconsulting.com</p>
  </section>

  <section class="card card--back" aria-label="Card back">
    <div class="back__mark">Mara Quill</div>
    <div class="holder">
      <p class="holder__name">MARA QUILL</p>
      <p class="holder__role">Owner</p>
    </div>
    <ul class="contact">
      <li class="contact__item">
        <svg class="contact__icon" viewBox="0 0 12 12" aria-hidden="true"><path d="M2.5 0.5l2 2.2-1 1.3c0.8 1.7 2 2.9 3.5 3.6l1.3-1 2.2 2-1.3 2.4C4.8 10.6 1.2 7 0.5 2z"/></svg>
        610-555-0147
      </li>
      <li class="contact__item">
        <svg class="contact__icon" viewBox="0 0 12 12" aria-hidden="true"><path d="M0.5 2h11v8h-11z M1 2.5l5 4 5-4" fill="none" stroke="#2b2b2b" stroke-width="1.2"/></svg>
        mara@maraquillconsulting.com
      </li>
      <li class="contact__item">
        <svg class="contact__icon" viewBox="0 0 12 12" aria-hidden="true"><circle cx="6" cy="6" r="5.3"/><path d="M0.8 6h10.4M6 0.8c-2.2 2.8-2.2 7.6 0 10.4M6 0.8c2.2 2.8 2.2 7.6 0 10.4" fill="none" stroke="#f7f7f6" stroke-width="0.8"/></svg>
        www.maraquillconsulting.com
      </li>
    </ul>
  </section>
</body>
</html>
```